Modernise Business Card

Our company has been operating for 10 years. With the start of the new decade we are looking to refresh our business card design. We manufacture a range of industrial product shipping to customers internationally. A copy of our current card, both sides, is attached. We are looking for a mature professional appearance.

```html
<!DOCTYPE html>
<html lang="en">
<head>
<meta charset="utf-8">
<title>Vantrel Business Card</title>
<link href="https://fonts.googleapis.com/css2?family=Roboto:wght@400;500;700;900&display=swap" rel="stylesheet">
<style>
  :root {
    --brand-blue: #00acd6;
    --ink: #1f2326;
    --paper: #ffffff;
    --backdrop: #6b7478;
    --backdrop-light: #9aa3a7;
  }
  * { margin: 0; padding: 0; box-sizing: border-box; }
  html, body { width: 1200px; height: 900px; overflow: hidden; }
  body {
    background: radial-gradient(ellipse at 45% 50%, var(--backdrop-light), var(--backdrop) 75%);
    font-family: 'Roboto', Arial, sans-serif;
    position: relative;
  }
  .card {
    position: absolute;
    width: 620px;
    height: 354px;
    left: 290px;
    background: var(--paper);
    box-shadow: 0 12px 30px rgba(0,0,0,0.35);
    overflow: hidden;
  }
  .card-front { top: 70px; }
  .card-back { top: 476px; }

  /* Front */
  .front-band-top {
    position: absolute; left: 0; top: 0; width: 100%; height: 132px;
    background: var(--brand-blue);
    border-bottom: 4px solid var(--ink);
  }
  .front-band-bottom {
    position: absolute; left: 0; bottom: 0; width: 100%; height: 78px;
    background: var(--brand-blue);
    border-top: 4px solid var(--ink);
  }
  .front-wordmark {
    position: absolute; left: 0; width: 100%; top: 52px;
    text-align: center;
    font-weight: 900; font-size: 72px; letter-spacing: -1px;
    color: var(--paper);
  }
  .front-services {
    position: absolute; left: 0; width: 100%; top: 160px;
    text-align: center; list-style: none;
    color: var(--brand-blue); font-size: 22px; line-height: 34px;
  }
  .front-web {
    position: absolute; left: 0; width: 100%; bottom: 26px;
    text-align: center; color: var(--paper); font-size: 17px; letter-spacing: 0.5px;
  }

  /* Back */
  .back-shapes { position: absolute; inset: 0; }
  .back-wordmark {
    position: absolute; left: 40px; top: 66px;
    font-weight: 900; font-size: 60px; letter-spacing: -1px;
    color: var(--brand-blue);
  }
  .holder-name {
    position: absolute; left: 300px; top: 40px; width: 250px; height: 54px;
    line-height: 54px; text-align: center;
    color: var(--paper); font-weight: 700; font-size: 24px;
  }
  .contact-list {
    position: absolute; left: 40px; bottom: 36px; list-style: none;
    color: var(--ink); font-size: 16px; line-height: 28px;
  }
  .contact-list li { display: flex; align-items: center; gap: 12px; }
  .contact-list svg { width: 16px; height: 16px; fill: var(--brand-blue); flex: none; }
  .address {
    position: absolute; left: 392px; right: 14px; bottom: 56px;
    text-align: center; color: var(--paper); font-size: 12px; line-height: 19px;
    white-space: nowrap;
  }
  .address svg { width: 16px; height: 20px; fill: var(--paper); display: block; margin: 0 auto 8px; }
</style>
</head>
<body>

<section class="card card-front">
  <div class="front-band-top"></div>
  <div class="front-band-bottom"></div>
  <div class="front-wordmark">Vantrel</div>
  <ul class="front-services">
    <li>HYDRAULIC ADAPTERS</li>
    <li>HOSE FITTINGS</li>
    <li>QUICK COUPLINGS</li>
  </ul>
  <div class="front-web">www.vantrelfittings.com</div>
</section>

<section class="card card-back">
  <svg class="back-shapes" viewBox="0 0 620 354" width="620" height="354">
    <polygon points="320,0 620,0 620,354 380,354" fill="var(--brand-blue)"/>
    <polygon points="300,94 330,94 330,116" fill="#0d1012"/>
    <rect x="300" y="40" width="250" height="54" fill="var(--ink)"/>
  </svg>
  <div class="back-wordmark">Vantrel</div>
  <div class="holder-name">Alan Brandt</div>
  <ul class="contact-list">
    <li><svg viewBox="0 0 16 16"><path d="M3 1l3 3-2 2c1 2 3 4 5 5l2-2 3 3-2 3C7 15 1 9 1 3z"/></svg>+86 135 2207 4481 (China)</li>
    <li><svg viewBox="0 0 16 16"><path d="M2 5c0-2 12-2 12 0v2h-3V5H5v2H2z M4 8h8l2 6H2z"/></svg>+61 412 387 905 (Australia)</li>
    <li><svg viewBox="0 0 16 16"><path d="M1 3h14v10H1z M1 3l7 6 7-6" stroke="#fff" stroke-width="1"/></svg>abrandt@vantrelfittings.com</li>
    <li><svg viewBox="0 0 16 16"><circle cx="8" cy="8" r="7"/><path d="M1 8h14M8 1c3 3 3 11 0 14M8 1c-3 3-3 11 0 14" stroke="#fff" stroke-width="1" fill="none"/></svg>www.vantrelfittings.com</li>
  </ul>
  <div class="address">
    <svg viewBox="0 0 16 20"><path d="M8 0a7 7 0 0 1 7 7c0 5-7 13-7 13S1 12 1 7a7 7 0 0 1 7-7z M8 4a3 3 0 1 0 0 6 3 3 0 0 0 0-6z" fill-rule="evenodd"/></svg>
    1208-3, Rong Tai Building<br>
    146 Hexing Road, Jiangbei District<br>
    Ningbo 315020 China
  </div>
</section>

</body>
</html>
```